Business Card Design

Hi we are an MMA and fitness gym, we would like a design similar to the themes in the logo provided and with all the information on it as well.
Updates

1. The phone number is 0455 612 907
2. The address is 18 Calloway street

Hi some of the designs have the wrong phone number the correct number is 0417 583 640

the correct address is 18 Calloway Street 

Industry/Entity Type

Fitness

Contact Information for Business Card

Danielle Fairow
Club Manager
0417 583 640
18 Calloway Street Wynnum Central
Qld 4178
gym@ironvalemma.com.au
www.ironvalemma.com.au

MMA, Boxing, Muay Thai, Kids MMA, BlazeRun group fitness

```html
<!DOCTYPE html>
<html lang="en">
<head>
<meta charset="utf-8">
<title>Ironvale MMA Gym – Business Cards</title>
<link href="https://fonts.googleapis.com/css2?family=Roboto+Condensed:wght@300;400;700&family=Roboto:wght@700&display=swap" rel="stylesheet">
<style>
  :root {
    --page-bg: #1a2523;
    --card-black: #070809;
    --metal-dark: #111315;
    --metal-mid: #3a3d40;
    --metal-light: #6a6d70;
    --text-white: #ffffff;
    --text-soft: #c9cbcd;
    --text-grey: #a4a7aa;
    --logo-grey: #d9dadb;
    --accent-blue: #2fa6e6;
    --accent-glow: #7fd3ff;
  }
  * { margin: 0; padding: 0; box-sizing: border-box; }
  html, body {
    width: 1200px;
    height: 1045px;
    overflow: hidden;
    background: var(--page-bg);
  }
  .canvas {
    position: relative;
    width: 1200px;
    height: 1045px;
    font-family: "Roboto Condensed", sans-serif;
  }

  /* Front card */
  .card-front {
    position: absolute;
    left: 215px;
    top: 115px;
    width: 641px;
    height: 348px;
    background:
      linear-gradient(90deg, var(--metal-dark) 0%, #1c1e20 35%, var(--metal-mid) 75%, var(--metal-light) 100%),
      var(--metal-dark);
    overflow: hidden;
  }
  .card-front::after {
    content: "";
    position: absolute;
    inset: 0;
    background: repeating-linear-gradient(0deg, rgba(255,255,255,0.03) 0 1px, rgba(0,0,0,0.05) 1px 3px);
  }
  .front-brand {
    position: absolute;
    left: 0;
    right: 0;
    top: 108px;
    display: flex;
    align-items: center;
    justify-content: center;
    gap: 14px;
    z-index: 1;
  }
  .brand-dot {
    width: 18px;
    height: 18px;
    border-radius: 50%;
    background: var(--logo-grey);
  }
  .brand-name {
    color: var(--logo-grey);
    font-weight: 700;
    font-size: 44px;
    letter-spacing: 2px;
    text-transform: uppercase;
    line-height: 1;
  }
  .front-web {
    position: absolute;
    left: 0;
    right: 0;
    top: 265px;
    text-align: center;
    color: var(--text-soft);
    font-size: 16px;
    font-weight: 400;
    z-index: 1;
  }
  .front-services {
    position: absolute;
    left: 0;
    right: 0;
    top: 295px;
    text-align: center;
    color: var(--text-grey);
    font-size: 25px;
    font-weight: 300;
    z-index: 1;
  }

  /* Back card */
  .card-back {
    position: absolute;
    left: 410px;
    top: 503px;
    width: 680px;
    height: 370px;
    background: linear-gradient(90deg, var(--card-black) 0%, #121416 55%, #1e2124 100%);
    overflow: hidden;
  }
  .glow-band {
    position: absolute;
    right: 0;
    width: 370px;
    height: 20px;
    background: linear-gradient(90deg, rgba(47,166,230,0) 0%, var(--accent-blue) 35%, var(--accent-glow) 100%);
  }
  .glow-band.top { top: 2px; }
  .glow-band.bottom { bottom: 4px; }
  .accent-line {
    position: absolute;
    right: 0;
    top: 44px;
    width: 380px;
    height: 2px;
    background: linear-gradient(90deg, rgba(47,166,230,0), var(--accent-blue));
  }
  .accent-line.lower { top: auto; bottom: 48px; }
  .smoke {
    position: absolute;
    right: 0;
    top: 0;
    width: 380px;
    height: 370px;
    background: radial-gradient(ellipse at 75% 30%, rgba(47,166,230,0.22), rgba(47,166,230,0) 60%),
                radial-gradient(ellipse at 70% 90%, rgba(47,166,230,0.28), rgba(47,166,230,0) 55%);
  }
  .back-brand {
    position: absolute;
    left: 350px;
    top: 168px;
    width: 320px;
    display: flex;
    align-items: center;
    justify-content: center;
    gap: 12px;
  }
  .back-brand .brand-name { font-size: 38px; }
  .back-brand .brand-dot { width: 16px; height: 16px; }

  .contact {
    position: absolute;
    left: 26px;
    top: 92px;
    color: var(--text-white);
  }
  .contact-name {
    font-family: "Roboto", sans-serif;
    font-weight: 700;
    font-size: 31px;
    line-height: 1;
  }
  .contact-role {
    margin-top: 14px;
    font-size: 18px;
    font-weight: 400;
  }
  .contact-list {
    list-style: none;
    margin-top: 36px;
    font-size: 19px;
    font-weight: 400;
  }
  .contact-list li { height: 31px; }
</style>
</head>
<body>
<main class="canvas">
  <section class="card-front">
    <div class="front-brand">
      <span class="brand-dot"></span>
      <span class="brand-name">Ironvale MMA Gym</span>
    </div>
    <p class="front-web">www.ironvalemma.com.au</p>
    <p class="front-services">MMA, Boxing, Muay Thai, Kids MMA, BlazeRun group fitness</p>
  </section>

  <section class="card-back">
    <div class="smoke" role="img" aria-label="Soft blue smoke glow behind the gym name"></div>
    <div class="glow-band top" role="img" aria-label="Glowing blue segmented band"></div>
    <div class="accent-line"></div>
    <div class="accent-line lower"></div>
    <div class="glow-band bottom" role="img" aria-label="Glowing blue segmented band"></div>

    <div class="back-brand">
      <span class="brand-dot"></span>
      <span class="brand-name">Ironvale MMA Gym</span>
    </div>

    <div class="contact">
      <h1 class="contact-name">Danielle Fairow</h1>
      <p class="contact-role">Club Manager</p>
      <ul class="contact-list">
        <li>18 Calloway st</li>
        <li>gym@ironvalemma.com.au</li>
        <li>0417 583 640</li>
        <li>www.ironvalemma.com.au</li>
      </ul>
    </div>
  </section>
</main>
</body>
</html>
```